Business Card Design - Cryotherapy

We need a custom created business card for our company FrostLeaf Spa. We provide whole body cryotherapy and localized cryotherapy to our clients. Please be creative.
Please see our website for idea's on design.
www.frostleafspa-example.com
Industry/Entity Type
Business
Contact Information for Business Card
Name, Position, Phone Number, Address, Website, Email
Look and feel
Each slider illustrates characteristics of the customer's brand and the style your logo design should communicate.

```html
<!DOCTYPE html>
<html lang="en">
<head>
<meta charset="utf-8">
<title>FrostLeaf Spa — Business Card</title>
<link rel="stylesheet" href="https://fonts.googleapis.com/css2?family=Josefin+Sans:wght@500&family=Libre+Baskerville&family=Roboto+Mono:ital,wght@1,500&display=swap">
<style>
  :root {
    --page-bg: #eeeae4;
    --card-light: #e4eef3;
    --card-mid: #cddfe7;
    --card-deep: #b9d1dc;
    --brand-green: #12875a;
    --brand-teal: #0f9aa0;
    --ink: #2b2f33;
    --icon-bg: #f8bd4c;
    --seal-black: #111111;
    --seal-ring: #0f8a6e;
  }
  * { margin: 0; padding: 0; box-sizing: border-box; }
  html, body { width: 1200px; height: 1200px; overflow: hidden; }
  body { background: var(--page-bg); position: relative; }

  .card {
    position: absolute;
    left: 280px;
    width: 640px;
    height: 367px;
    border-radius: 22px;
    overflow: hidden;
    background: linear-gradient(135deg, var(--card-light) 0%, var(--card-mid) 55%, var(--card-deep) 100%);
    box-shadow: 0 6px 14px rgba(0,0,0,0.18);
  }
  .card--front { top: 173px; }
  .card--back { top: 600px; }

  .front-brand {
    position: absolute;
    left: 22px;
    top: 62px;
    display: flex;
    align-items: center;
    gap: 12px;
  }
  .front-brand__dot {
    width: 30px; height: 30px; border-radius: 50%;
    background: var(--brand-teal);
  }
  .brand-name {
    font-family: "Josefin Sans", sans-serif;
    font-weight: 500;
    color: var(--brand-green);
    letter-spacing: 1px;
  }
  .front-brand .brand-name { font-size: 38px; }

  .contact-list {
    position: absolute;
    left: 42px;
    top: 170px;
    list-style: none;
  }
  .contact-item {
    display: flex;
    align-items: flex-start;
    gap: 20px;
    margin-bottom: 22px;
  }
  .contact-icon {
    width: 31px; height: 31px;
    border-radius: 4px;
    background: var(--icon-bg);
    flex: none;
    display: flex; align-items: center; justify-content: center;
  }
  .contact-text {
    font-family: "Libre Baskerville", serif;
    font-size: 13px;
    line-height: 16px;
    color: var(--ink);
    letter-spacing: 1px;
    padding-top: 1px;
  }

  .back-band {
    position: absolute;
    left: 0; right: 0;
    top: 158px;
    height: 27px;
    background: linear-gradient(90deg, var(--brand-green), var(--brand-teal));
  }
  .back-seal {
    position: absolute;
    left: 197px;
    top: 48px;
    width: 246px; height: 246px;
    border-radius: 50%;
    background: var(--seal-black);
    border: 10px solid var(--seal-ring);
    display: flex; align-items: center; justify-content: center;
  }
  .back-seal .brand-name { font-size: 30px; }
  .back-url {
    position: absolute;
    left: 0; right: 0;
    top: 302px;
    text-align: center;
    font-family: "Roboto Mono", monospace;
    font-style: italic;
    font-weight: 500;
    font-size: 15px;
    letter-spacing: 4px;
    color: var(--ink);
    text-transform: uppercase;
  }
</style>
</head>
<body>
  <section class="card card--front">
    <div class="front-brand">
      <span class="front-brand__dot"></span>
      <span class="brand-name">FrostLeaf Spa</span>
    </div>
    <ul class="contact-list">
      <li class="contact-item">
        <span class="contact-icon">
          <svg width="18" height="18" viewBox="0 0 24 24" aria-hidden="true"><path fill="#fff" d="M6.6 10.8a15.1 15.1 0 0 0 6.6 6.6l2.2-2.2c.3-.3.7-.4 1-.2 1.1.4 2.3.6 3.6.6.6 0 1 .4 1 1V20c0 .6-.4 1-1 1A17 17 0 0 1 3 4c0-.6.4-1 1-1h3.5c.6 0 1 .4 1 1 0 1.3.2 2.5.6 3.6.1.3 0 .7-.2 1z"/></svg>
        </span>
        <span class="contact-text">(555), 204-7193</span>
      </li>
      <li class="contact-item">
        <span class="contact-icon">
          <svg width="20" height="20" viewBox="0 0 24 24" aria-hidden="true" fill="none" stroke="#fff" stroke-width="1.8"><circle cx="12" cy="12" r="9"/><ellipse cx="12" cy="12" rx="4" ry="9"/><path d="M3 12h18M4.5 7.5h15M4.5 16.5h15"/></svg>
        </span>
        <span class="contact-text">info@frostleafspa-example.com<br>www.frostleafspa-example.com</span>
      </li>
      <li class="contact-item">
        <span class="contact-icon">
          <svg width="18" height="18" viewBox="0 0 24 24" aria-hidden="true"><path fill="#fff" d="M12 2a7 7 0 0 0-7 7c0 5.2 7 13 7 13s7-7.8 7-13a7 7 0 0 0-7-7zm0 9.5A2.5 2.5 0 1 1 12 6.5a2.5 2.5 0 0 1 0 5z"/></svg>
        </span>
        <span class="contact-text">720 Birchwood Lane<br>Suite 210<br>Lakeview, IL 60099</span>
      </li>
    </ul>
  </section>

  <section class="card card--back">
    <div class="back-band"></div>
    <div class="back-seal">
      <span class="brand-name">FrostLeaf Spa</span>
    </div>
    <p class="back-url">www.frostleafspa-example.com</p>
  </section>
</body>
</html>
```